Property Finance Company - Orin Ventures Limited

Background: Orin Ventures Group Limited is a private property finance company. Orin Ventures Group has capital to directly fund first mortgage, mezzanine and preferred equity financing. We also acquire performing, sub-performing and distressed debt.

Orin Ventures' management philosophy emphasises expertise, innovation, wisdom, honesty and competitiveness. Orin Ventures are not finance brokers - we provide debt funding to the commercial property and residential development sectors. Our process is built from experience and cumutavely Orin Ventures' Directors have in excess of 60 years wisdom.

The aim of the website will be to increase brand awareness, provide clients with comfort around our level of skill and background on who we are, generate more sales, and provide examples of projects that we have funded.

The website is a new product launch, and we need to use our Orin Ventures logo that has just been designed. We like a dark background, and either black/silver/grey/ jade green, or black/gold/jade green colours.

Our unique advantages are that we have fast turnaround times, we can solve clients funding problems and we know what we are doing. Our target audience will be viewing the website on both desktop and mobile devices.

We would like to have the following pages:

Home
About
Team
Services
Project Experience
Contact

Competitors Website: http://www.tarvelo.com/

We would also like to have the option of video footage in our website, as you can see in our competitors website.

Overall we want a really slick, elegant but modern website that is better than www.tarvelo.com

Target Market(s)

Finance borrowers, property developers, accountants, lawyers, businesspeople, high net worth people

Industry/Entity Type

Finance

Requirements
Must have
• Please see project description
Nice to have
Should not have

```html
<!DOCTYPE html>
<html lang="en">
<head>
<meta charset="utf-8">
<title>Orin Ventures Group — Private Property Finance</title>
<link rel="stylesheet" href="https://fonts.googleapis.com/css2?family=Oswald:wght@400;500&family=Open+Sans:wght@400;600&display=swap">
<style>
:root{
  --jade:#1b615b;
  --jade-dark:#134a45;
  --ink:#0b0f12;
  --night:#10181c;
  --steel-1:#3a3a3a;
  --steel-2:#555555;
  --steel-3:#6a6a6a;
  --white:#ffffff;
  --text-grey:#555b60;
  --field-line:#a9a9a9;
}
*{box-sizing:border-box;margin:0;padding:0}
html,body{width:1200px;height:2885px;overflow:hidden}
body{position:relative;background:var(--ink);font-family:"Open Sans",Arial,sans-serif;color:var(--white)}
.abs{position:absolute}
.heading{font-family:"Oswald","Arial Narrow",sans-serif;font-weight:400;text-transform:uppercase;letter-spacing:.5px}

/* Hero */
.hero{left:0;top:0;width:1200px;height:596px;background:linear-gradient(135deg,#4a4f55 0%,#2c3136 40%,#3d4248 65%,#23272b 100%)}
.hero-shade{left:0;top:0;width:1200px;height:596px;background:linear-gradient(180deg,rgba(0,0,0,.35),rgba(0,0,0,.15) 50%,rgba(0,0,0,.4))}
.brand{left:78px;top:56px;width:140px;text-align:center;font-family:"Oswald","Arial Narrow",sans-serif;font-size:19px;line-height:22px;color:var(--white);letter-spacing:1px}
.brand-mark{display:block;width:34px;height:34px;border-radius:50%;background:var(--white);margin:-30px auto 8px}
.brand small{display:block;font-size:11px;letter-spacing:3px;line-height:14px}
.nav{left:0;top:64px;width:1200px;height:34px}
.nav a{position:absolute;top:0;height:34px;line-height:34px;color:var(--white);text-decoration:none;font-size:17px;transform:translateX(-50%);white-space:nowrap}
.nav a.current{border:2px solid var(--white);border-radius:17px;padding:0 20px;line-height:30px}
.hero-play{left:567px;top:246px}
.hero-title{left:0;top:348px;width:1200px;text-align:center;font-family:"Oswald","Arial Narrow",sans-serif;font-size:50px;line-height:62px;font-weight:400}
.hero-sub{left:0;top:414px;width:1200px;text-align:center;font-family:"Oswald","Arial Narrow",sans-serif;font-size:31px;line-height:40px}
.slider-dots{left:97px;top:502px}

/* About */
.about{left:0;top:596px;width:1200px;height:429px;background:linear-gradient(180deg,var(--steel-2),var(--steel-3) 50%,var(--steel-2))}
.about-photo{left:117px;top:662px;width:292px;height:292px;border-radius:50%;border:4px solid #cfcfcf;background:radial-gradient(circle at 40% 40%,#7f93a8,#33465a 70%)}
.about-title{left:438px;top:692px;font-size:34px;line-height:42px}
.about-text{left:438px;top:744px;width:640px;font-size:14.5px;line-height:26px;color:#f1f1f1}
.btn{display:block;background:var(--jade);color:var(--white);text-transform:uppercase;text-align:center;border-radius:17px;font-size:12px;text-decoration:none}
.about-btn{left:438px;top:894px;width:102px;height:33px;line-height:33px}

/* Services */
.services{left:0;top:1025px;width:1200px;height:613px;background:linear-gradient(180deg,#0d1a1e,#15272c 50%,#0b1417)}
.services-title{left:0;top:1098px;width:1200px;text-align:center;font-size:34px;line-height:46px}
.card{top:1188px;width:316px;height:364px;background:var(--white);text-align:center}
.card-photo{margin:12px 12px 0;height:192px}
.card h3{margin-top:26px;font-weight:400;font-size:19px;color:#222;line-height:24px}
.card p{margin:10px auto 0;width:270px;font-size:13.5px;line-height:23px;color:var(--text-grey)}
.card .more{display:block;margin-top:10px;font-size:13.5px;color:var(--jade);text-decoration:none}
.arrow{top:1334px}

/* Project experience */
.projects{left:0;top:1638px;width:1200px;height:539px;background:linear-gradient(180deg,var(--steel-1),#5a5a5a 50%,var(--steel-1))}
.project-box{left:123px;top:1752px;width:958px;height:327px;background:var(--white)}
.project-title{left:165px;top:1810px;font-size:32px;line-height:42px;color:#1a1a1a}
.project-text{left:165px;top:1860px;width:430px;font-size:14.5px;line-height:22.5px;color:var(--text-grey)}
.project-btn{left:165px;top:1992px;width:110px;height:33px;line-height:33px}
.project-media{left:629px;top:1752px;width:452px;height:327px;background:linear-gradient(135deg,#d9dde2,#a7b0ba 55%,#6d747c)}

/* Contact */
.contact{left:0;top:2177px;width:1200px;height:512px;background:linear-gradient(180deg,#1d1f21,#141618)}
.contact-title{left:0;top:2262px;width:1200px;text-align:center;font-size:31px;line-height:42px}
.contact-sub{left:0;top:2313px;width:1200px;text-align:center;font-size:16px;line-height:24px}
.field{height:54px;border:1.5px solid var(--field-line);padding-left:18px;line-height:51px;font-size:14px;color:#eaeaea}
.submit{left:527px;top:2590px;width:127px;height:39px;line-height:39px;border-radius:20px;font-size:17px;text-transform:none}

/* Footer */
.footer{left:0;top:2689px;width:1200px;height:196px;background:#030303}
.social{top:2756px;width:34px;height:34px;border:2px solid var(--white);border-radius:50%}
.copyright{left:0;top:2803px;width:1200px;text-align:center;font-size:13px;line-height:20px}
</style>
</head>
<body>

<section class="abs hero" role="img" aria-label="Business people reviewing financial charts on a laptop"></section>
<div class="abs hero-shade"></div>

<div class="abs brand"><span class="brand-mark"></span>ORIN VENTURES<small>GROUP</small></div>

<nav class="abs nav">
  <a class="current" href="#" style="left:437px">Home</a>
  <a href="#" style="left:540px">About</a>
  <a href="#" style="left:642px">Team</a>
  <a href="#" style="left:752px">Services</a>
  <a href="#" style="left:915px">Project Experience</a>
  <a href="#" style="left:1077px">Contact</a>
</nav>

<svg class="abs hero-play" width="66" height="66" viewBox="0 0 66 66">
  <circle cx="33" cy="33" r="31" fill="rgba(0,0,0,.55)" stroke="#fff" stroke-width="2"/>
  <path d="M26 19 L48 33 L26 47 Z" fill="#fff"/>
</svg>
<h1 class="abs hero-title">Orin Ventures Group</h1>
<p class="abs hero-sub">A private property finance company</p>
<svg class="abs slider-dots" width="56" height="26" viewBox="0 0 56 26">
  <circle cx="13" cy="13" r="12" fill="rgba(0,0,0,.55)"/><path d="M15 8 L10 13 L15 18" stroke="#fff" stroke-width="2" fill="none"/>
  <circle cx="42" cy="13" r="12" fill="rgba(0,0,0,.55)"/><path d="M40 8 L45 13 L40 18" stroke="#fff" stroke-width="2" fill="none"/>
</svg>

<section class="abs about"></section>
<div class="abs about-photo" role="img" aria-label="Smiling businessman at a meeting table"></div>
<h2 class="abs heading about-title">About Us</h2>
<p class="abs about-text">Orin Ventures Group Limited is a private property finance company. Orin Ventures Group has capital to directly fund first mortgage, mezzanine and preferred equity financing. We also acquire performing, sub-performing and distressed debt. Orin Ventures' management philosophy emphasises expertise, innovation, wisdom, honesty and competitiveness. Orin Ventures are not finance brokers - we provide debt funding to the commercial property and residential development sectors.</p>
<a class="abs btn about-btn" href="#">Read More &raquo;</a>

<section class="abs services"></section>
<h2 class="abs heading services-title">Our Services</h2>

<article class="abs card" style="left:88px">
  <div class="card-photo" role="img" aria-label="Colleagues shaking hands over documents and a laptop" style="background:linear-gradient(135deg,#8a7a6c,#c9b8a4 50%,#5d5650)"></div>
  <h3>Porro Quisquam</h3>
  <p>The point of using Lorem Ipsum is that it has a more-or-less normal</p>
  <a class="more" href="#">Read More &raquo;</a>
</article>
<article class="abs card" style="left:444px">
  <div class="card-photo" role="img" aria-label="Presenter showing charts on a whiteboard to a team" style="background:linear-gradient(135deg,#d8dcd8,#9aa4a6 55%,#3b4450)"></div>
  <h3>Dolorem Ipsum</h3>
  <p>The point of using Lorem Ipsum is that it has a more-or-less normal</p>
  <a class="more" href="#">Read More &raquo;</a>
</article>
<article class="abs card" style="left:800px">
  <div class="card-photo" role="img" aria-label="Tablet displaying floating blue bar charts" style="background:linear-gradient(135deg,#e4f2fb,#7dbfe6 50%,#2f7fbf)"></div>
  <h3>Neque Porro</h3>
  <p>The point of using Lorem Ipsum is that it has a more-or-less normal</p>
  <a class="more" href="#">Read More &raquo;</a>
</article>

<svg class="abs arrow" style="left:46px" width="24" height="40" viewBox="0 0 24 40"><path d="M20 2 L4 20 L20 38" stroke="#fff" stroke-width="2.5" fill="none"/></svg>
<svg class="abs arrow" style="left:1130px" width="24" height="40" viewBox="0 0 24 40"><path d="M4 2 L20 20 L4 38" stroke="#fff" stroke-width="2.5" fill="none"/></svg>

<section class="abs projects"></section>
<div class="abs project-box"></div>
<h2 class="abs heading project-title">Project Experience</h2>
<p class="abs project-text">It is a long established fact that a reader will be distracted by the readable content of a page when looking at its layout. The point of using Lorem Ipsum is that it has a more-or-less normal distribution of letters, as opposed to using 'Content here, content here', making it look like readable English</p>
<a class="abs btn project-btn" href="#">Read More</a>
<div class="abs project-media" role="img" aria-label="Hands using a tablet over financial papers"></div>
<svg class="abs" style="left:820px;top:1880px" width="70" height="70" viewBox="0 0 70 70">
  <circle cx="35" cy="35" r="33" fill="rgba(0,0,0,.5)"/>
  <path d="M27 21 L51 35 L27 49 Z" fill="#fff"/>
</svg>

<section class="abs contact"></section>
<h2 class="abs heading contact-title">Contact Us</h2>
<p class="abs contact-sub">Neque porro quisquam est qui dolorem ipsum quia dolor sit amet</p>
<div class="abs field" style="left:190px;top:2381px;width:410px">First Name</div>
<div class="abs field" style="left:613px;top:2381px;width:408px">LastName</div>
<div class="abs field" style="left:190px;top:2446px;width:410px">Phone</div>
<div class="abs field" style="left:613px;top:2446px;width:408px">Email address</div>
<div class="abs field" style="left:190px;top:2511px;width:831px">Message</div>
<a class="abs btn submit" href="#">Submit</a>

<footer class="abs footer"></footer>
<span class="abs social" style="left:471px" aria-label="Social link"></span>
<span class="abs social" style="left:516px" aria-label="Social link"></span>
<span class="abs social" style="left:560px" aria-label="Social link"></span>
<span class="abs social" style="left:604px" aria-label="Social link"></span>
<span class="abs social" style="left:648px" aria-label="Social link"></span>
<svg class="abs" style="left:693px;top:2756px" width="34" height="34" viewBox="0 0 34 34" aria-label="Email">
  <circle cx="17" cy="17" r="16" fill="none" stroke="#fff" stroke-width="2"/>
  <rect x="10" y="12" width="14" height="10" fill="none" stroke="#fff" stroke-width="1.6"/>
  <path d="M10 12 L17 18 L24 12" fill="none" stroke="#fff" stroke-width="1.6"/>
</svg>
<p class="abs copyright">Copyright © 2017&nbsp; All Rights Reserved</p>

</body>
</html>
```